Hosvin Logo and business card

We need a business card and logo, we are currently using a logo that we like but would like to be a bit more streamlined. We deal with very high end clients and our business card needs to reflect that. We would love to see and hire somebody that can deliver a very MODERN, simple design. With he main front of the card to be black with either a red lettering or White to provide great contrast. I would like to have a minimalist abstract picture of a heavy machine on it but it is not a requirement ( most likely an Crane ( a brisk otter crane with a bucket would be perfect or maybe a vendrel 820 TX )) If it keeps in line with being a classic simple, and modern design. Letterpress is also an option where it gives it a great look and texture, the card will be printed on a thick stock. On the back there needs to be a star included somewhere on the card and design, this represents the first generation that started the company back in 1936 therefore it is a sentimental addition ( make it modern and simple)
We do not want a cheesy construction template. We do heavy site work, aka we use excavators, payloaders, off road jox m41 trucks, very big fun toys.
There is a huge chance to get the web design as well for the winning design.
Have fun, cannot wait to see the designs!
In addition, we'd like to point out that our primary need and priority is still the BUSINESS CARD design itself. The logo has to complement the overall look of the business card, but it is secondary to the card's look. Please keep this in mind.
Thank you,
Gideon
Target Market(s)
General Contractors, upscale home owners ( house values of 1M plus)
and commercial property owners.
Projects range from $5000 to 1 million.
Industry/Entity Type
Construction
Requirements
Must have
- Star incorporated into design
Nice to have
- an abstract heavy site work machine ( pics attached) If it keeps in line with being a classic simple, and modern design.
I would like to have black and red on the design since all the lettering on the trucks is red, but i will let the designer take care of that.

```html
<!DOCTYPE html>
<html lang="en">
<head>
<meta charset="utf-8">
<title>Hosvin Business Card</title>
<link rel="stylesheet" href="https://fonts.googleapis.com/css2?family=Michroma&display=swap">
<style>
  :root {
    --backdrop: #1b1b1c;
    --card: #1f1f20;
    --card-band: #111112;
    --red: #d8201c;
    --grey: #6b6b6b;
    --grey-light: #7d7d7d;
  }
  * { margin: 0; padding: 0; box-sizing: border-box; }
  html, body {
    width: 1200px; height: 849px; overflow: hidden;
    background: var(--backdrop);
    font-family: "Michroma", sans-serif;
  }
  .stage {
    position: relative; width: 1200px; height: 849px;
    display: flex; align-items: center; justify-content: center; gap: 60px;
  }
  .card {
    position: relative; width: 520px; height: 297px;
    background: var(--card);
    box-shadow: 0 18px 40px rgba(0,0,0,.55);
    overflow: hidden;
  }
  .brand {
    display: flex; align-items: center; gap: 10px;
    color: var(--red); text-transform: uppercase; letter-spacing: 2px;
    white-space: nowrap;
  }
  .brand-dot {
    flex: none; width: 8px; height: 8px; border-radius: 50%; background: var(--red);
  }
  .card-back .brand {
    position: absolute; left: 50%; top: 50%;
    transform: translate(-50%, -50%);
    font-size: 30px;
  }
  .card-front .brand {
    position: absolute; left: 30px; top: 52px; font-size: 20px;
  }
  .identity {
    position: absolute; right: 30px; top: 118px; text-align: right;
  }
  .person-name {
    color: var(--red); font-size: 15px; letter-spacing: 1.5px; text-transform: uppercase;
  }
  .person-title {
    color: var(--grey); font-size: 10px; letter-spacing: 1px; margin-top: 4px; text-transform: uppercase;
  }
  .contact {
    position: absolute; right: 30px; top: 180px; text-align: right;
    color: var(--grey-light); font-size: 9.5px; letter-spacing: 1px; line-height: 1.7;
    text-transform: uppercase; white-space: nowrap;
  }
  .card-band {
    position: absolute; left: 0; right: 0; bottom: 0; height: 58px;
    background: var(--card-band);
  }
</style>
</head>
<body>
  <main class="stage">
    <section class="card card-back" aria-label="Card back">
      <div class="brand"><span class="brand-dot"></span><span class="brand-name">Hosvin</span></div>
    </section>

    <section class="card card-front" aria-label="Card front">
      <div class="brand"><span class="brand-dot"></span><span class="brand-name">Hosvin</span></div>
      <div class="identity">
        <p class="person-name">Name Surname</p>
        <p class="person-title">Title</p>
      </div>
      <div class="contact">
        <p>Phone: 0000 0000 000 &nbsp;E-mail: aaaaaa@hosvin.com</p>
        <p>www.hosvin.com</p>
      </div>
      <div class="card-band"></div>
    </section>
  </main>
</body>
</html>
```